Radiant Harbor Chocolate Shake Label

We need a new label design for our Radiant Harbor Chocolate Protein Shake. The design needs to include all the composition info as per the attached Lumo Grace Chocolate shake label with a fresh new eye catching design that will stand out on retail store shelves. It must include our Radiant Harbor Logo and portray a professional image that inspires trust. It must indicate that it is a chocolate shake that looks tasty and inviting. Radiant Harbor is a product sold by healthcare practitioners.

Industry/Entity Type

Health And Wellness

Requirements
Must have
• The Radiant Harbor logo. Contain all the attached info as per the chocolate Lumo Grace label. Feature something that indicates it is a chocolate shake on the label that looks tasty and inviting.
Nice to have
• I have attached some of the other products in our range. Would be a bonus if it can match into the existing look and feel somehow.

```html
<!DOCTYPE html>
<html lang="en">
<head>
<meta charset="utf-8">
<title>Radiant Harbor Chocolate Protein Shake Label</title>
<link rel="stylesheet" href="https://fonts.googleapis.com/css2?family=Open+Sans:wght@600;800&family=Roboto:wght@500&display=swap">
<style>
  :root {
    --canvas: #f3f1ee;
    --label-white: #ffffff;
    --caramel: #c2702f;
    --caramel-deep: #a9581f;
    --caramel-light: #d98a44;
    --cocoa-text: #4a2a17;
    --milk-choc: #b98a66;
    --milk-choc-light: #e3cdbb;
    --brand-blue: #2e4a78;
  }
  html, body {
    margin: 0;
    padding: 0;
    width: 1200px;
    height: 1200px;
    overflow: hidden;
    background: var(--canvas);
  }
  .canvas {
    position: relative;
    width: 1200px;
    height: 1200px;
  }
  .label {
    position: absolute;
    left: 77px;
    top: 192px;
    width: 1045px;
    height: 815px;
    display: block;
  }
  .label-base { fill: var(--label-white); }
  .top-band { fill: url(#bandGradient); }
  .brand-tab { fill: var(--label-white); }
  .brand-mark { fill: var(--brand-blue); }
  .brand-name {
    font-family: "Open Sans", Arial, sans-serif;
    font-weight: 600;
    font-size: 46px;
    fill: var(--brand-blue);
  }
  .product-title {
    font-family: "Open Sans", Arial, sans-serif;
    font-weight: 800;
    font-size: 132px;
    fill: var(--caramel);
  }
  .divider-line { stroke: var(--caramel); fill: none; }
  .flavour-line {
    font-family: "Roboto", Arial, sans-serif;
    font-weight: 500;
    font-size: 44px;
    fill: var(--cocoa-text);
  }
  .bottom-rule { stroke: var(--caramel); stroke-width: 5; }
</style>
</head>
<body>
<main class="canvas">
  <svg class="label" viewBox="0 0 1045 815" xmlns="http://www.w3.org/2000/svg" aria-label="Radiant Harbor Protein Shake, Chocolate Flavour Shake label">
    <defs>
      <linearGradient id="bandGradient" x1="0" y1="0" x2="1" y2="0">
        <stop offset="0" stop-color="var(--caramel-deep)"/>
        <stop offset="0.5" stop-color="var(--caramel)"/>
        <stop offset="1" stop-color="var(--caramel-light)"/>
      </linearGradient>
      <linearGradient id="chocolateGradient" x1="0" y1="0" x2="0" y2="1">
        <stop offset="0" stop-color="var(--milk-choc)"/>
        <stop offset="0.7" stop-color="var(--milk-choc)"/>
        <stop offset="1" stop-color="var(--milk-choc-light)"/>
      </linearGradient>
    </defs>

    <rect class="label-base" x="0" y="0" width="1045" height="815"/>

    <!-- Top band with brand tab -->
    <rect class="top-band" x="0" y="0" width="1045" height="154"/>
    <path class="brand-tab" d="M187 154 V70 Q187 48 209 48 H770 L803 154 Z"/>
    <circle class="brand-mark" cx="262" cy="104" r="26"/>
    <text class="brand-name" x="302" y="120">Radiant Harbor</text>

    <!-- Product name -->
    <text class="product-title" x="26" y="398" textLength="972" lengthAdjust="spacingAndGlyphs" transform="rotate(-5 26 398)">PROTEIN SHAKE</text>

    <!-- Chocolate milk splash area -->
    <path role="img" aria-label="Chocolate milkshake splash illustration" fill="url(#chocolateGradient)" d="M0 480 L1045 350 V640 H0 Z"/>

    <!-- Divider lines -->
    <line class="divider-line" x1="0" y1="470" x2="1045" y2="338" stroke-width="7"/>
    <line class="divider-line" x1="0" y1="452" x2="1045" y2="320" stroke-width="2"/>

    <!-- Flavour -->
    <text class="flavour-line" x="187" y="530" textLength="592" lengthAdjust="spacingAndGlyphs" transform="rotate(-4 187 530)">Chocolate Flavour Shake</text>

    <!-- Bottom rule -->
    <line class="bottom-rule" x1="0" y1="803" x2="1045" y2="803"/>
  </svg>
</main>
</body>
</html>
```